Construction Company Website

I need a website for my construction company
Target Market(s)
People looking for construction work
Coding
Coded - Design and coding required
Number of Pages Required
4 page
Colors
0455a3
ffc214
Requirements
Must have
- A home page about my company,
A completed projects page showcasing some completed works
A contact me page with an enquiry form
Nice to have
- Professional and contemporary whilst classy website.

```html
<!DOCTYPE html>
<html lang="en">
<head>
<meta charset="utf-8">
<title>Ridgeline Construction</title>
<link rel="stylesheet" href="https://fonts.googleapis.com/css2?family=Montserrat:wght@400;500;600;700&family=Open+Sans:wght@400;600&display=swap">
<style>
:root{
  --blue:#0455a3;
  --yellow:#ffc214;
  --ink:#3a3a3a;
  --muted:#6b6b6b;
  --light:#f1f1f1;
  --grey-band:#e9e9e9;
  --footer:#151515;
  --footer-base:#0a0a0a;
  --white:#ffffff;
}
*{box-sizing:border-box;margin:0;padding:0}
html,body{width:1200px;height:3576px;overflow:hidden}
body{font-family:"Open Sans",Arial,sans-serif;color:var(--ink);background:var(--white);position:relative}
.section-title{font-family:"Montserrat",Arial,sans-serif;font-weight:500;color:var(--blue);font-size:38px;text-align:center;letter-spacing:1px}
.btn{display:inline-block;background:var(--yellow);color:#222;font-family:"Montserrat",Arial,sans-serif;font-weight:600;font-size:17px;text-transform:uppercase;padding:0 34px;line-height:58px;text-decoration:none}

/* hero */
.hero{position:absolute;left:0;top:0;width:1200px;height:662px;
  background:linear-gradient(180deg,#8f9ba7 0%,#6e7a6a 30%,#55604c 48%,#8a8a84 62%,#a9a7a1 100%)}
.hero::after{content:"";position:absolute;inset:0;background:rgba(20,25,30,.35)}
.brand-box{position:absolute;left:140px;top:0;width:165px;height:140px;background:#101d2e;z-index:2;display:flex;align-items:center;justify-content:center;gap:8px;padding:0 10px}
.brand-box .mark{width:14px;height:14px;background:var(--yellow);flex:none}
.brand-name{font-family:"Montserrat",Arial,sans-serif;font-weight:600;color:var(--yellow);font-size:15px;letter-spacing:1px;line-height:1.2;text-transform:uppercase}
.main-nav{position:absolute;right:90px;top:34px;z-index:2;display:flex;gap:28px}
.main-nav a{font-family:"Montserrat",Arial,sans-serif;color:var(--white);font-size:15px;font-weight:600;text-decoration:none;text-transform:uppercase}
.main-nav a.active{color:var(--yellow)}
.hero-content{position:absolute;left:0;right:0;top:275px;z-index:2;text-align:center;color:var(--white)}
.hero-title{font-family:"Montserrat",Arial,sans-serif;font-weight:500;font-size:64px;letter-spacing:2px}
.hero-tag{font-size:17px;line-height:1.5;margin:14px auto 38px;width:640px}

/* about */
.about{position:absolute;left:0;top:662px;width:1200px;height:648px}
.about-bar{position:absolute;left:95px;top:108px;width:55px;height:440px;background:var(--yellow)}
.about-bar span{position:absolute;left:50%;top:50%;transform:translate(-50%,-50%) rotate(-90deg);white-space:nowrap;font-family:"Montserrat",Arial,sans-serif;font-size:22px;font-weight:500;color:#222;letter-spacing:1px}
.about-photo{position:absolute;left:150px;top:108px;width:370px;height:440px;background:linear-gradient(160deg,#7ea0c4 0%,#9a6a52 35%,#86503d 60%,#6a7a55 100%)}
.about-text{position:absolute;left:600px;top:105px;width:520px}
.about-text h2{font-family:"Montserrat",Arial,sans-serif;font-weight:500;color:var(--blue);font-size:38px;margin-bottom:22px}
.about-text p{font-size:15px;line-height:1.7;color:var(--muted);margin-bottom:10px}
.about-text .btn{margin-top:16px;font-size:15px;line-height:54px;padding:0 30px}

/* services */
.services{position:absolute;left:0;top:1310px;width:1200px;height:670px;background:var(--grey-band)}
.services .section-title{position:absolute;top:40px;left:0;right:0}
.service-cards{position:absolute;top:130px;left:92px;display:flex;gap:28px}
.service-card{width:320px;height:340px;background:var(--white);box-shadow:0 2px 6px rgba(0,0,0,.12);position:relative;text-align:center}
.service-card .photo{height:170px;position:relative}
.service-card .photo svg{position:absolute;left:0;bottom:-1px;width:320px;height:50px}
.service-card h3{font-family:"Montserrat",Arial,sans-serif;font-weight:500;color:var(--blue);font-size:20px;margin:24px 0 10px}
.service-card p{font-size:13px;line-height:1.6;color:var(--muted);padding:0 30px}
.service-card .more{display:block;margin-top:12px;font-size:13px;font-weight:600;color:#333;text-transform:uppercase}
.service-card.featured{background:var(--blue)}
.service-card.featured h3,.service-card.featured p,.service-card.featured .more{color:var(--white)}
.dots{position:absolute;top:622px;left:0;right:0;display:flex;justify-content:center;gap:8px}
.dots i{width:14px;height:14px;border-radius:50%;border:2px solid var(--blue)}
.dots i.on{background:var(--blue)}

/* testimonials */
.testimonials{position:absolute;left:0;top:1980px;width:1200px;height:510px}
.testimonials .section-title{position:absolute;top:85px;left:0;right:0}
.quote{position:absolute;top:165px;width:465px;height:190px;background:var(--light);padding:30px 34px;font-size:16px;line-height:1.6;color:#444}
.quote::after{content:"";position:absolute;left:40px;bottom:-20px;border-left:24px solid transparent;border-right:24px solid transparent;border-top:20px solid var(--light)}
.author{position:absolute;top:385px;display:flex;align-items:center;gap:16px}
.avatar{width:62px;height:62px;border-radius:50%;background:linear-gradient(135deg,#8a7a6a,#4a4038)}
.author strong{display:block;font-family:"Montserrat",Arial,sans-serif;color:var(--blue);font-weight:600;font-size:17px;text-transform:uppercase}
.author small{display:block;font-size:13px;color:#555;text-transform:uppercase}
.stars{display:flex;gap:2px;margin-top:3px}

/* gallery */
.gallery{position:absolute;left:0;top:2490px;width:1200px;height:670px}
.gallery .section-title{position:absolute;top:50px;left:0;right:0}
.gallery .tile{position:absolute}

/* footer */
.site-footer{position:absolute;left:0;top:3160px;width:1200px;height:340px;background:var(--footer);color:#cfcfcf}
.footer-brand{position:absolute;left:165px;top:70px;width:150px;display:flex;flex-direction:column;align-items:center;gap:10px}
.footer-brand .mark{width:60px;height:60px;background:var(--yellow)}
.socials{display:flex;gap:10px;margin-top:10px}
.socials i{width:20px;height:20px;background:#cfcfcf;border-radius:3px}
.footer-col{position:absolute;top:75px}
.footer-col h4{font-family:"Montserrat",Arial,sans-serif;font-weight:500;color:var(--white);font-size:22px;margin-bottom:18px;text-transform:uppercase}
.footer-col li{list-style:none;font-size:14px;line-height:28px}
.copyright{position:absolute;left:0;top:3500px;width:1200px;height:76px;background:var(--footer-base);color:#dcdcdc;font-size:15px;text-align:center;line-height:76px}
</style>
</head>
<body>

<header class="hero" role="img" aria-label="Photo of a finished concrete slab in a fenced garden">
  <div class="brand-box"><span class="mark"></span><span class="brand-name">Ridgeline<br>Construction</span></div>
  <nav class="main-nav">
    <a class="active" href="#">Home</a><a href="#">About Us</a><a href="#">Services</a><a href="#">Testimonial</a><a href="#">Gallery</a><a href="#">Contact Us</a>
  </nav>
  <div class="hero-content">
    <h1 class="hero-title">RIDGELINE CONSTRUCTION</h1>
    <p class="hero-tag">Lorem ipsum dolor sit amet, consectetur adipiscing elit, sed do eiusmod tempor incididunt ut labore et dolore magna aliqua.</p>
    <a class="btn" href="#">Get Started</a>
  </div>
</header>

<section class="about">
  <div class="about-bar"><span>Ridgeline Construction</span></div>
  <div class="about-photo" role="img" aria-label="Photo of a brick house extension"></div>
  <div class="about-text">
    <h2>ABOUT US</h2>
    <p>Lorem ipsum dolor sit amet, consectetur adipiscing elit, sed do eiusmod tempor incididunt ut labore et dolore magna aliqua. Ut enim ad minim veniam, quis nostrud exercitation ullamco laboris nisi ut aliquip ex ea commodo consequat. Duis aute irure dolor in reprehenderit in voluptate velit esse cillum dolore eu fugiat nulla pariatur. Excepteur sint occaecat cupidatat non proident, sunt in culpa qui officia deserunt mollit anim id est laborum.</p>
    <p>Sed ut perspiciatis unde omnis iste natus error sit voluptatem accusantium doloremque laudantium, totam rem aperiam, eaque.</p>
    <a class="btn" href="#">Read More</a>
  </div>
</section>

<section class="services">
  <h2 class="section-title">SERVICES</h2>
  <div class="service-cards">
    <article class="service-card">
      <div class="photo" role="img" aria-label="Photo of a wet concrete driveway" style="background:linear-gradient(160deg,#6d7884,#3e4650 60%,#8b8b86)">
        <svg viewBox="0 0 320 50" preserveAspectRatio="none"><path d="M0 20 Q160 58 320 20 L320 50 L0 50Z" fill="#fff"/><path d="M0 20 Q160 58 320 20" fill="none" stroke="#ffc214" stroke-width="5"/></svg>
      </div>
      <h3>FINIBUS BONORUM</h3>
      <p>Lorem ipsum dolor sit amet, consectetur adipiscing elit, sed do eiusmod tempor incididunt ut labore et dolore magna.</p>
      <span class="more">Read More</span>
    </article>
    <article class="service-card featured">
      <div class="photo" role="img" aria-label="Photo of a renovated interior room" style="background:linear-gradient(160deg,#d9d4cc,#a8272e 55%,#c9c3ba)">
        <svg viewBox="0 0 320 50" preserveAspectRatio="none"><path d="M0 20 Q160 58 320 20 L320 50 L0 50Z" fill="#0455a3"/><path d="M0 20 Q160 58 320 20" fill="none" stroke="#fff" stroke-width="5"/></svg>
      </div>
      <h3>BONORUM ET MALORUM</h3>
      <p>Lorem ipsum dolor sit amet, consectetur adipiscing elit, sed do eiusmod tempor incididunt ut labore et dolore magna.</p>
      <span class="more">Read More</span>
    </article>
    <article class="service-card">
      <div class="photo" role="img" aria-label="Photo of a brick house exterior" style="background:linear-gradient(170deg,#9fb4c9,#7c4a3a 55%,#5e6a4a)">
        <svg viewBox="0 0 320 50" preserveAspectRatio="none"><path d="M0 20 Q160 58 320 20 L320 50 L0 50Z" fill="#fff"/><path d="M0 20 Q160 58 320 20" fill="none" stroke="#ffc214" stroke-width="5"/></svg>
      </div>
      <h3>BONORUM ET MALORUM</h3>
      <p>Lorem ipsum dolor sit amet, consectetur adipiscing elit, sed do eiusmod tempor incididunt ut labore et dolore magna.</p>
      <span class="more">Read More</span>
    </article>
  </div>
  <div class="dots"><i></i><i class="on"></i><i></i></div>
</section>

<section class="testimonials">
  <h2 class="section-title">TESTIMONIALS</h2>
  <blockquote class="quote" style="left:120px">Lorem ipsum dolor sit amet, consectetur adipiscing elit, sed do eiusmod tempor incididunt ut labore et dolore magna aliqua. Ut enim ad minim veniam, quis nostrud exercitation ullamco</blockquote>
  <blockquote class="quote" style="left:615px">Lorem ipsum dolor sit amet, consectetur adipiscing elit, sed do eiusmod tempor incididunt ut labore et dolore magna aliqua. Ut enim ad minim veniam, quis nostrud exercitation ullamco</blockquote>
  <div class="author" style="left:135px">
    <div class="avatar" role="img" aria-label="Client portrait"></div>
    <div><strong>Owen Castillo</strong><small>Customer Clients</small>
      <div class="stars"><svg width="90" height="16" viewBox="0 0 90 16"><g fill="#ffc214"><path id="st" d="M8 0l2.4 5 5.6.7-4 3.8 1 5.5L8 12.4 3 15l1-5.5-4-3.8 5.6-.7z"/><use href="#st" x="18"/><use href="#st" x="36"/><use href="#st" x="54"/><use href="#st" x="72"/></g></svg></div>
    </div>
  </div>
  <div class="author" style="left:630px">
    <div class="avatar" role="img" aria-label="Client portrait"></div>
    <div><strong>Daniel Hartley</strong><small>Customer Clients</small>
      <div class="stars"><svg width="90" height="16" viewBox="0 0 90 16"><g fill="#ffc214"><use href="#st"/><use href="#st" x="18"/><use href="#st" x="36"/><use href="#st" x="54"/><use href="#st" x="72"/></g></svg></div>
    </div>
  </div>
</section>

<section class="gallery">
  <h2 class="section-title">GALLERY</h2>
  <div class="tile" role="img" aria-label="Photo of a house build site with materials" style="left:92px;top:130px;width:448px;height:460px;background:linear-gradient(170deg,#a9b9c6,#8a6a55 45%,#9a968c)"></div>
  <div class="tile" role="img" aria-label="Photo of a new garden wall and patio" style="left:556px;top:130px;width:272px;height:228px;background:linear-gradient(170deg,#b6c6d4,#7e8a6a 50%,#a39e94)"></div>
  <div class="tile" role="img" aria-label="Photo of a newly built swimming pool" style="left:556px;top:374px;width:272px;height:216px;background:linear-gradient(170deg,#9a9488,#3aa7d6 45%,#c8c2b6)"></div>
  <div class="tile" role="img" aria-label="Photo of a brick house rear view" style="left:844px;top:130px;width:264px;height:220px;background:linear-gradient(170deg,#c1ccd6,#8a5a46 60%)"></div>
  <div class="tile" role="img" aria-label="Photo of groundworks with block foundations" style="left:844px;top:360px;width:264px;height:230px;background:linear-gradient(170deg,#8c8a84,#7a5c46 50%,#6e6458)"></div>
</section>

<footer class="site-footer">
  <div class="footer-brand">
    <span class="mark"></span>
    <span class="brand-name">Ridgeline</span>
    <div class="socials"><i></i><i></i><i></i><i></i></div>
  </div>
  <div class="footer-col" style="left:416px">
    <h4>Quick Links</h4>
    <ul><li>Home</li><li>About Us</li><li>Services</li><li>Testimonial</li><li>Gallery</li><li>Contact Us</li></ul>
  </div>
  <div class="footer-col" style="left:660px">
    <h4>Services</h4>
    <ul><li>Finibus Bonorum</li><li>Bonorum Et Malorum</li><li>Bonorum Et Malorum</li><li>Finibus Bonorum</li></ul>
  </div>
  <div class="footer-col" style="left:912px">
    <h4>Contact Us</h4>
    <ul><li>4820 Cedar Mill Rd</li><li>Fairview, GA 30499</li><li>555-014-2736</li><li>hello@ridgeline-build.example</li></ul>
  </div>
</footer>
<div class="copyright">Copyright © 2020 Ridgeline Construction. All Rights Reserved.</div>

</body>
</html>
```